Brightwell Acupuncture Studio Website Design

We are working with Brightwell Acunpuncture Studio. They are a local Chinese medicine and acupuncture studio and in need of a new website design.

Some sites to use for inspiration:

https://marbleriveracupuncture.example
https://cedarglowacupuncture.example
https://quietharborclinic.example
https://emberfieldacupuncture.example
https://fernhollowclinic.example

Thank you for taking the time to consider designing a website for us. We are web developers based in Stockton, CA, USA. Most of our projects go through the same process. Understanding this process may help you win a project with us. We custom-code all of our websites in-house. We don’t have any requirements as to what tools you use for your design, but we prefer Figma files. For any design that we label as four-stars, we send it to the client for review. The client picks the final design they want us to use. Once we complete this process, we will continue to show additional clients all the four-star sites and purchase them later. Your designs will have multiple chances to sell. For better chances of success, we ask that you follow these guidelines.

IMAGES:
If you use any images or icons in the design, we ask that you have a link to the asset so we can purchase the image/icon. Most of the designs we submit do not have the customer’s images on them unless they have some great images. Be creative; show us the feeling you are trying to portray with your image choices. Use any royalty-free site you choose. We subscribe to Vantrel and mainly use their images, but we can purchase images outside of Vantrel.

PLEASE NOTE: we will not submit designs to clients with watermarks on the images.

FONTS:
We ask that you identify the fonts used in the design. This can be done in a message if you want. We typically use Google Fonts and Vantrel Fonts.

CONTENT:
We're always open to different content and ideas. We often submit designs with stock images so the client can see our vision. We typically take pictures after the website launch to use their images with our vision. Lorem Ipsum is fine for paragraphs, but we ask that you write the headers in correct English. We want to be able to show the vision and identify the sections of the website.

INSPIRATION:
We typically add a couple of links in the brief of websites we like to help you get started in your design.

REVISIONS:
We do not often ask for revisions of the designs unless we see something in the design that may not appeal to the client. If there are slight changes that we want to make, we do that in the development process.

FEEDBACK:
We rarely give feedback on designs during the design process. We are working on many website projects and do not have the time to provide feedback. We usually respond if your request is well thought out and asks specific questions, but a note asking “feedback, please” usually goes unanswered.

```html
<!DOCTYPE html>
<html lang="en">
<head>
<meta charset="utf-8">
<title>Brightwell Acupuncture Studio</title>
<link href="https://fonts.googleapis.com/css2?family=Poppins:ital,wght@0,300;0,400;0,500;0,600;0,700;1,600&display=swap" rel="stylesheet">
<style>
:root{
  --coral:#e0615a;
  --coral-soft:#e98a83;
  --coral-pale:#f6d3cf;
  --navy:#26303b;
  --footer:#2b3540;
  --ink:#2a2f36;
  --text:#5a5f66;
  --white:#ffffff;
}
*{margin:0;padding:0;box-sizing:border-box}
html,body{width:1200px;height:5333px;overflow:hidden;background:var(--white)}
body{font-family:'Poppins',sans-serif;color:var(--ink)}
.page{position:relative;width:1200px;height:5333px;overflow:hidden}
.abs{position:absolute}
.btn{position:absolute;display:flex;align-items:center;justify-content:center;border-radius:30px;background:var(--navy);color:var(--white);font-size:13px;font-weight:500;letter-spacing:.3px;text-transform:uppercase;border:2px solid var(--navy);box-shadow:5px 0 0 -1px var(--coral)}
.rule{position:absolute;height:2px;background:var(--coral)}
.rule::after{content:"";position:absolute;right:-3px;top:-3px;width:8px;height:8px;border-radius:50%;background:var(--coral)}

/* header */
.brand{position:absolute;display:flex;align-items:center;gap:12px}
.brand-dot{width:54px;height:54px;border-radius:50%;border:3px solid var(--coral);flex:none}
.brand-name{font-weight:500;color:var(--ink);line-height:1}
.nav{position:absolute;left:400px;top:60px;display:flex;gap:46px;font-size:12px;font-weight:500;text-transform:uppercase;color:var(--ink)}
.nav .active{border-left:2px solid var(--coral);padding-left:10px;font-weight:600}

/* hero */
.hero{position:absolute;left:0;top:138px;width:1200px;height:920px;
  background:
   radial-gradient(ellipse 260px 220px at 980px 130px,rgba(226,190,170,.95),rgba(226,190,170,0) 70%),
   radial-gradient(ellipse 330px 260px at 760px 360px,rgba(222,196,182,.95),rgba(222,196,182,0) 72%),
   radial-gradient(ellipse 300px 240px at 930px 640px,rgba(205,195,190,.95),rgba(205,195,190,0) 70%),
   radial-gradient(ellipse 520px 200px at 420px 700px,rgba(236,236,238,.95),rgba(236,236,238,0) 72%),
   radial-gradient(ellipse 260px 360px at 1080px 40px,rgba(28,44,74,.95),rgba(28,44,74,0) 70%),
   linear-gradient(100deg,#1c2a42 0%,#2f3e55 32%,#6d7684 55%,#b7b3b0 78%,#d9d4cf 100%)}
.hero-shade{position:absolute;left:0;top:138px;width:700px;height:560px;background:linear-gradient(90deg,rgba(20,30,48,.55),rgba(20,30,48,0))}
.hero-welcome{left:67px;top:246px;color:var(--coral);font-size:28px}
.hero-title{left:64px;top:276px;color:var(--white);font-size:92px;font-weight:700;line-height:1.1}
.hero-sub{left:67px;top:378px;color:var(--white);font-size:40px;font-weight:400}
.hero-text{left:67px;top:444px;color:var(--white);font-size:19px;line-height:29px;width:420px}
.hero-btn{left:67px;top:538px;width:190px;height:50px;background:transparent;border-color:var(--coral)}

/* about */
.h-big{font-size:64px;font-weight:600;color:var(--ink);line-height:1}
.h-sub{font-size:30px;font-weight:400;color:var(--ink)}
.body-copy{font-size:13px;line-height:24px;color:var(--text)}

/* services */
.svc{position:absolute;width:300px}
.svc-icon{width:100px;height:100px;border-radius:50%;background:var(--coral);border:4px solid var(--coral-pale);display:flex;align-items:center;justify-content:center}
.svc h3{font-size:20px;font-weight:400;margin-top:30px;color:var(--ink)}
.svc .mini{width:44px;height:2px;background:var(--coral);margin:14px 0 16px}
.svc p{font-size:13px;line-height:24px;color:var(--text)}

/* healing */
.healing{left:67px;top:2750px;width:1068px;height:502px;border-radius:30px;overflow:hidden;
  background:
   radial-gradient(ellipse 300px 200px at 880px 260px,rgba(39,160,180,1),rgba(39,160,180,0) 75%),
   radial-gradient(ellipse 200px 140px at 930px 60px,rgba(200,160,140,.9),rgba(200,160,140,0) 75%),
   radial-gradient(ellipse 420px 110px at 300px 440px,rgba(120,84,66,.95),rgba(120,84,66,0) 75%),
   radial-gradient(ellipse 260px 90px at 600px 330px,rgba(40,44,52,.9),rgba(40,44,52,0) 75%),
   linear-gradient(90deg,#f2efec 0%,#e8e3df 40%,#c9cfd0 62%,#3aa6b6 80%,#2a95a6 100%)}
.play{left:568px;top:2910px;width:62px;height:62px;border-radius:50%;border:2px solid var(--coral);background:var(--white);display:flex;align-items:center;justify-content:center}

/* conditions */
.cond{position:absolute;top:3592px;width:257px;height:263px}
.cond-label{position:absolute;left:0;right:0;bottom:28px;text-align:center;font-size:17px;font-weight:600;color:var(--ink);text-transform:uppercase}

/* testimonial */
.testi{left:0;top:4055px;width:1200px;height:660px;
  background:
   radial-gradient(ellipse 380px 180px at 560px 560px,rgba(150,110,92,.85),rgba(150,110,92,0) 75%),
   radial-gradient(ellipse 260px 160px at 340px 160px,rgba(190,160,145,.7),rgba(190,160,145,0) 75%),
   radial-gradient(ellipse 160px 260px at 980px 260px,rgba(170,150,145,.6),rgba(170,150,145,0) 75%),
   linear-gradient(180deg,#7c7e83 0%,#5f6268 45%,#45484f 100%)}
.testi-shade{left:0;top:4055px;width:1200px;height:660px;background:rgba(40,44,52,.35)}
.arrow{position:absolute;width:22px;height:22px;border-left:2px solid var(--white);border-bottom:2px solid var(--white)}

/* footer */
.footer{left:0;top:4715px;width:1200px;height:618px;background:var(--footer)}
.news{left:67px;top:4795px;width:1080px;height:143px;border-radius:72px;background:var(--coral)}
.foot-h{font-size:19px;font-weight:500;color:var(--white)}
.foot-list{list-style:none;font-size:13px;color:var(--white)}
.foot-list li{display:flex;align-items:center;gap:10px;height:32px}
.foot-list li::before{content:"";width:12px;height:12px;border-radius:50%;border:2px solid var(--coral)}
.contact-row{position:absolute;left:845px;display:flex;gap:14px;font-size:12.5px;color:var(--white);line-height:15px}
.contact-ico{width:22px;height:22px;border:1.5px solid var(--coral);border-radius:3px;display:flex;align-items:center;justify-content:center;flex:none}
.social{position:absolute;top:5183px;width:38px;height:38px;border:2px solid var(--white);border-radius:6px;display:flex;align-items:center;justify-content:center}
.social span{width:12px;height:12px;border-radius:50%;background:var(--white)}
</style>
</head>
<body>
<div class="page">

  <!-- header -->
  <div class="brand" style="left:55px;top:38px">
    <div class="brand-dot"></div>
    <div>
      <div class="brand-name" style="font-size:30px">Brightwell</div>
      <div class="brand-name" style="font-size:17px;margin-top:5px;letter-spacing:1px">Acupuncture Studio</div>
    </div>
  </div>
  <nav class="nav">
    <span class="active">Home</span><span>About</span><span>Services</span><span>Testimonials</span><span>Contact Us</span>
  </nav>
  <div class="btn" style="left:956px;top:48px;width:178px;height:42px;font-size:12px">Book Appointment</div>

  <!-- hero -->
  <section class="hero" role="img" aria-label="Photo of a practitioner placing acupuncture needles on a relaxed client's face"></section>
  <div class="hero-shade"></div>
  <svg class="abs" style="left:0;top:860px" width="1200" height="220" viewBox="0 0 1200 220" aria-hidden="true">
    <path d="M0 40 Q600 320 1200 40 L1200 220 L0 220Z" fill="#fff"/>
    <path d="M0 60 Q600 330 1200 30" fill="none" stroke="#e0615a" stroke-width="12"/>
  </svg>
  <div class="abs hero-welcome">Welcome To</div>
  <div class="abs hero-title">Brightwell</div>
  <div class="abs hero-sub">Acupuncture Studio</div>
  <div class="abs hero-text">Lorem ipsum dolor sit amet, consectetur adipiscing elit, sed do eiusmod tempor</div>
  <div class="btn hero-btn">Book Appointment</div>
  <div class="abs" style="left:573px;top:961px;display:flex;gap:5px">
    <span style="width:20px;height:6px;border-radius:3px;background:var(--navy)"></span>
    <span style="width:6px;height:6px;border-radius:50%;background:var(--navy)"></span>
    <span style="width:6px;height:6px;border-radius:50%;background:var(--navy)"></span>
    <span style="width:6px;height:6px;border-radius:50%;background:var(--navy)"></span>
  </div>

  <!-- about -->
  <div class="abs h-big" style="left:112px;top:1212px">About Us</div>
  <div class="abs h-sub" style="left:112px;top:1280px">Who We Are</div>
  <div class="rule" style="left:112px;top:1336px;width:178px"></div>
  <p class="abs body-copy" style="left:112px;top:1368px;width:430px">Lorem ipsum dolor sit amet, consectetur adipiscing elit, sed do eiusmod tempor incididunt ut labore et dolore magna aliqua. Quis ipsum suspendisse ultrices gravida. Risus commodo viverra maecenas accumsan lacus vel facilisis. Lorem ipsum dolor sit amet, consectetur adipiscing elit, sed do eiusmod tempor incididunt ut labore et dolore magna aliqua. Quis ipsum suspendisse ultrices gravida. Risus commodo viverra maecenas accumsan lacus vel facilisis.</p>
  <div class="btn" style="left:112px;top:1595px;width:152px;height:48px">Know More</div>
  <div class="abs" role="img" aria-label="Illustration of acupuncture needles arranged around a circular treatment photo" style="left:585px;top:1130px;width:615px;height:485px;background:
     radial-gradient(circle 165px at 420px 235px,#dfe9f1 0%,#eed8cf 45%,rgba(238,216,207,0) 100%),
     radial-gradient(circle 205px at 420px 235px,rgba(196,128,104,0) 78%,rgba(196,128,104,.75) 84%,rgba(196,128,104,0) 92%),
     radial-gradient(ellipse 300px 260px at 380px 250px,#f7ebe6 0%,#ffffff 100%)"></div>

  <!-- services -->
  <div class="abs h-big" style="left:0;width:1200px;text-align:center;top:1838px">Our Services</div>
  <div class="abs h-sub" style="left:0;width:1200px;text-align:center;top:1908px">What We Do</div>
  <div class="rule" style="left:505px;top:1963px;width:186px"></div>

  <div class="svc" style="left:90px;top:2053px">
    <div class="svc-icon" role="img" aria-label="Needles icon"><svg width="54" height="54" viewBox="0 0 54 54" fill="none" stroke="#fff" stroke-width="2" stroke-linecap="round"><line x1="14" y1="12" x2="24" y2="46"/><line x1="27" y1="8" x2="27" y2="46"/><line x1="40" y1="12" x2="30" y2="46"/><circle cx="14" cy="9" r="3"/><circle cx="27" cy="5" r="3"/><circle cx="40" cy="9" r="3"/><line x1="10" y1="48" x2="44" y2="48"/></svg></div>
    <h3>Whole-Body Acupuncture</h3><div class="mini"></div><p>Lorem ipsum dolor sit amet, consectetur adipiscing elit, sed do eiusmod tempor incididunt ut labore et</p></div>
  <div class="svc" style="left:452px;top:2053px">
    <div class="svc-icon" role="img" aria-label="Cosmetic care icon"><svg width="54" height="54" viewBox="0 0 54 54" fill="none" stroke="#fff" stroke-width="2" stroke-linejoin="round"><path d="M27 6 Q40 24 40 33 A13 13 0 0 1 14 33 Q14 24 27 6Z"/><path d="M42 8 L44 13 L49 15 L44 17 L42 22 L40 17 L35 15 L40 13Z"/><path d="M21 33 A6 6 0 0 0 27 39"/></svg></div>
    <h3>Cosmetic Acupuncture</h3><div class="mini"></div><p>Lorem ipsum dolor sit amet, consectetur adipiscing elit, sed do eiusmod tempor incididunt ut labore et</p></div>
  <div class="svc" style="left:815px;top:2053px">
    <div class="svc-icon" role="img" aria-label="Leaf and capsule icon"><svg width="54" height="54" viewBox="0 0 54 54" fill="none" stroke="#fff" stroke-width="2" stroke-linecap="round"><path d="M10 44 Q8 14 40 8 Q44 38 10 44Z"/><line x1="10" y1="44" x2="32" y2="18"/><rect x="28" y="30" width="22" height="10" rx="5" transform="rotate(-40 39 35)"/></svg></div>
    <h3>Functional Medicine</h3><div class="mini"></div><p>Lorem ipsum dolor sit amet, consectetur adipiscing elit, sed do eiusmod tempor incididunt ut labore et</p></div>
  <div class="svc" style="left:90px;top:2365px">
    <div class="svc-icon" role="img" aria-label="Micro roller icon"><svg width="54" height="54" viewBox="0 0 54 54" fill="none" stroke="#fff" stroke-width="2" stroke-linecap="round"><rect x="8" y="8" width="26" height="14" rx="4"/><line x1="14" y1="8" x2="14" y2="22"/><line x1="20" y1="8" x2="20" y2="22"/><line x1="26" y1="8" x2="26" y2="22"/><path d="M34 15 L40 15 L40 26 L30 40"/><line x1="30" y1="40" x2="24" y2="48"/></svg></div>
    <h3>Microneedling Acupuncture</h3><div class="mini"></div><p>Lorem ipsum dolor sit amet, consectetur adipiscing elit, sed do eiusmod tempor incididunt ut labore et</p></div>
  <div class="svc" style="left:452px;top:2365px">
    <div class="svc-icon" role="img" aria-label="Herbal bowl icon"><svg width="54" height="54" viewBox="0 0 54 54" fill="none" stroke="#fff" stroke-width="2" stroke-linecap="round"><path d="M8 28 L46 28 Q46 44 27 44 Q8 44 8 28Z"/><line x1="18" y1="48" x2="36" y2="48"/><line x1="30" y1="26" x2="44" y2="10"/><path d="M14 24 Q12 12 24 10 Q26 22 14 24Z"/></svg></div>
    <h3>Herbal Medicine</h3><div class="mini"></div><p>Lorem ipsum dolor sit amet, consectetur adipiscing elit, sed do eiusmod tempor incididunt ut labore et</p></div>
  <div class="svc" style="left:815px;top:2365px">
    <div class="svc-icon" role="img" aria-label="Energy waves icon"><svg width="54" height="54" viewBox="0 0 54 54" fill="none" stroke="#fff" stroke-width="2" stroke-linecap="round"><circle cx="27" cy="27" r="6"/><circle cx="27" cy="27" r="13"/><line x1="27" y1="4" x2="27" y2="10"/><line x1="27" y1="44" x2="27" y2="50"/><line x1="4" y1="27" x2="10" y2="27"/><line x1="44" y1="27" x2="50" y2="27"/><line x1="11" y1="11" x2="15" y2="15"/><line x1="39" y1="39" x2="43" y2="43"/><line x1="43" y1="11" x2="39" y2="15"/><line x1="15" y1="39" x2="11" y2="43"/></svg></div>
    <h3>PEMF Therapy</h3><div class="mini"></div><p>Lorem ipsum dolor sit amet, consectetur adipiscing elit, sed do eiusmod tempor incididunt ut labore et</p></div>

  <!-- healing journey -->
  <div class="abs healing" role="img" aria-label="Photo of a therapist in teal scrubs applying electro-acupuncture to a patient's back"></div>
  <div class="abs" style="left:114px;top:2800px;font-size:48px;font-weight:600;line-height:60px;color:var(--ink)">Beginning the<br>Healing Journey</div>
  <div class="rule" style="left:114px;top:2935px;width:180px"></div>
  <div class="abs" style="left:116px;top:2962px;width:360px;font-size:15px;line-height:27px;color:var(--ink)">Lorem ipsum dolor sit amet, consectetur adipiscing elit, sed do eiusmod tempor</div>
  <div class="abs play"><svg width="16" height="16" viewBox="0 0 16 16"><path d="M5 3 L12 8 L5 13Z" fill="#e0615a"/></svg></div>

  <!-- conditions -->
  <div class="abs" style="left:71px;top:3400px;font-size:34px;color:var(--ink)">Conditions</div>
  <div class="abs h-big" style="left:75px;top:3455px">We Treat</div>
  <div class="rule" style="left:380px;top:3500px;width:756px;height:1px;background:var(--coral-soft)"></div>

  <div class="cond" style="left:67px;background:radial-gradient(ellipse 70px 120px at 110px 120px,#c9a898,rgba(201,168,152,0) 80%),linear-gradient(180deg,#9fb3c4 0%,#c5d2dc 55%,#e6e4e0 100%)" role="img" aria-label="Photo of a woman meditating"><div class="cond-label">Mental Health</div></div>
  <div class="cond" style="left:340px;background:radial-gradient(ellipse 50px 40px at 130px 70px,#d2574e,rgba(210,87,78,0) 85%),radial-gradient(ellipse 100px 140px at 130px 150px,#c39c88,rgba(195,156,136,0) 80%),linear-gradient(180deg,#e4e4e4,#d6d2cf)" role="img" aria-label="Photo of a man holding his sore neck"><div class="cond-label">Chronic Pain</div></div>
  <div class="cond" style="left:607px;background:linear-gradient(180deg,#e8928b,#dd6d65)" role="img" aria-label="Photo of a woman with a coral overlay">
    <div style="position:absolute;top:38px;width:100%;text-align:center;font-size:17px;font-weight:500;color:#fff">HORMONAL HEALTH</div>
    <div style="position:absolute;top:92px;left:30px;right:30px;text-align:center;font-size:12px;line-height:24px;color:#fff">Lorem ipsum dolor sit amet, consectetur adipiscing elit, sed do eiusmod tempor</div>
    <div style="position:absolute;top:210px;width:100%;text-align:center;font-size:11px;font-weight:600;color:var(--ink)">READ MORE &rarr;</div>
  </div>
  <div class="cond" style="left:880px;background:radial-gradient(ellipse 40px 30px at 160px 180px,#d8443c,rgba(216,68,60,0) 85%),radial-gradient(ellipse 80px 130px at 200px 110px,#e9cbbd,rgba(233,203,189,0) 80%),linear-gradient(180deg,#eef1f4,#e4ddd9)" role="img" aria-label="Photo of a smiling woman holding a heart"><div class="cond-label">General Health</div></div>

  <div class="btn" style="left:497px;top:3925px;width:203px;height:50px">Book Appointment</div>

  <!-- testimonial -->
  <section class="abs testi" role="img" aria-label="Photo of a cupping therapy session on a client's back"></section>
  <div class="abs testi-shade"></div>
  <svg class="abs" style="left:0;top:4050px" width="1200" height="100" viewBox="0 0 1200 100" aria-hidden="true"><path d="M0 0 L1200 0 L1200 85 Q600 -40 0 85Z" fill="#fff"/></svg>
  <div class="abs" style="left:0;width:1200px;text-align:center;top:4190px;font-size:66px;font-weight:600;color:#fff">Our Testimonial</div>
  <div class="abs" style="left:0;width:1200px;text-align:center;top:4272px;font-size:30px;color:#fff">Client Reviews</div>
  <div class="abs" style="left:200px;top:4378px;font-size:40px;font-weight:700;color:#fff">&ldquo;</div>
  <p class="abs" style="left:230px;top:4402px;width:750px;text-align:center;font-size:16px;font-style:italic;font-weight:600;line-height:24px;color:#fff">Lorem ipsum dolor sit amet, consectetur adipiscing elit, sed do eiusmod tempor incididunt ut labore et dolore magna aliqua. Quis ipsum suspendisse ultrices gravida. Risus commodo viverra maecenas accumsan lacus vel facilisis.</p>
  <div class="arrow" style="left:128px;top:4430px;transform:rotate(45deg)"></div>
  <div class="arrow" style="left:1058px;top:4430px;transform:rotate(-135deg)"></div>
  <div class="abs" role="img" aria-label="Client portrait" style="left:518px;top:4505px;width:72px;height:72px;border-radius:50%;background:linear-gradient(180deg,#e8e8e8,#bfc3c8);border:3px solid #fff"></div>
  <div class="abs" style="left:602px;top:4528px;font-size:11px;font-weight:600;color:#fff">Daniel Marsh<br><span style="color:#f5c24c;letter-spacing:1px">★★★★★</span></div>
  <div class="abs" style="left:550px;top:4637px;display:flex;gap:12px;align-items:center">
    <span style="width:40px;height:6px;border-radius:3px;background:#fff"></span>
    <span style="width:8px;height:8px;border-radius:50%;background:#fff"></span>
    <span style="width:8px;height:8px;border-radius:50%;background:#fff"></span>
    <span style="width:8px;height:8px;border-radius:50%;background:#fff"></span>
  </div>

  <!-- footer -->
  <footer class="abs footer"></footer>
  <div class="abs news"></div>
  <div class="abs" style="left:110px;top:4838px;font-size:42px;font-weight:600;color:#fff">Our Newsletter Sign Up</div>
  <div class="abs" style="left:623px;top:4840px;width:474px;height:53px;border-radius:27px;background:#fff;font-size:12px;color:var(--text);padding:17px 32px">Enter Email Address</div>
  <div class="abs" style="left:955px;top:4840px;width:142px;height:53px;border-radius:27px;background:var(--navy);color:#fff;font-size:17px;display:flex;align-items:center;justify-content:center">SIGNUP</div>

  <div class="abs foot-h" style="left:235px;top:5028px">Quik Links</div>
  <div class="rule" style="left:235px;top:5068px;width:100px;height:1px"></div>
  <ul class="abs foot-list" style="left:242px;top:5090px">
    <li>Home</li><li>About Us</li><li>Services</li><li>Testimonials</li><li>Contact Us</li>
  </ul>

  <div class="brand" style="left:440px;top:5040px">
    <div class="brand-dot" style="width:70px;height:70px"></div>
    <div>
      <div class="brand-name" style="font-size:38px;color:#fff">Brightwell</div>
      <div class="brand-name" style="font-size:22px;color:#fff;margin-top:6px;letter-spacing:1px">Acupuncture Studio</div>
    </div>
  </div>
  <div class="social" style="left:510px" aria-label="Social link"><span></span></div>
  <div class="social" style="left:555px" aria-label="Social link"><span></span></div>
  <div class="social" style="left:600px" aria-label="Social link"><span></span></div>
  <div class="social" style="left:645px" aria-label="Social link"><span></span></div>

  <div class="abs foot-h" style="left:845px;top:5028px">Contact Details</div>
  <div class="rule" style="left:845px;top:5068px;width:155px;height:1px"></div>
  <div class="contact-row" style="top:5100px"><span class="contact-ico"><svg width="12" height="12" viewBox="0 0 12 12"><path d="M3 1 L5 4 L4 5 Q5 7 7 8 L8 7 L11 9 L10 11 Q4 11 1 2Z" fill="#e0615a"/></svg></span><span>CALL US<br>555 010 2468</span></div>
  <div class="contact-row" style="top:5155px"><span class="contact-ico"><svg width="12" height="10" viewBox="0 0 12 10"><rect x="0.5" y="0.5" width="11" height="9" fill="none" stroke="#e0615a"/><path d="M1 1 L6 6 L11 1" fill="none" stroke="#e0615a"/></svg></span><span>EMAIL US<br>hello@brightwellstudio.example</span></div>
  <div class="contact-row" style="top:5205px"><span class="contact-ico"><svg width="10" height="13" viewBox="0 0 10 13"><path d="M5 12 Q0 6 0 5 A5 5 0 0 1 10 5 Q10 6 5 12Z" fill="#e0615a"/><circle cx="5" cy="5" r="1.8" fill="#2b3540"/></svg></span><span>Address line here dummy<br>Address line here</span></div>

  <div class="abs" style="left:67px;top:5290px;width:1068px;height:1px;background:#4a5562"></div>
  <div class="abs" style="left:0;width:1200px;text-align:center;top:5307px;font-size:12px;color:#fff">Copyright ©2025. All Rights Reserved by Company name</div>

</div>
</body>
</html>
```